New Business Card : Logo provided (black&red)

Use logo to ascertain colours.
Front of card :
Logo
Director : Gareth Pollwick
ABN : 48392057
T : 0458 702 136
E : kinetrixx@postnest.com
W : kinetrixxfitness.com.au

Back of card :
Outdoor Group Training
Ferndale Archers Club
42 Tillbrook Road
Scarborough WA 6019

Personal Training
Amberline Fitness Studio
518 Wrenhollow Street
Scarborough WA 6019

Logo's attached are low resolution apparently so will look into why that is and update as soon as I can.  

Logo's updated.

```html
<!DOCTYPE html>
<html lang="en">
<head>
<meta charset="utf-8">
<title>Kinetrixx Fitness – Business Card</title>
<link href="https://fonts.googleapis.com/css2?family=Oswald:wght@300;400;500;600&display=swap" rel="stylesheet">
<style>
  :root {
    --page-bg: #ffffff;
    --card-front: #fbfbfb;
    --card-front-edge: #efefef;
    --card-back: #2b2b2b;
    --ink-dark: #1f1f1f;
    --ink-light: #ffffff;
    --brand-red: #d8262b;
    --brand-grey: #6b6b6b;
    --shadow: rgba(0, 0, 0, 0.28);
  }
  * { margin: 0; padding: 0; box-sizing: border-box; }
  html, body {
    width: 1000px; height: 1200px; overflow: hidden;
    background: var(--page-bg);
    font-family: "Oswald", "Arial Narrow", sans-serif;
  }
  .canvas { position: relative; width: 1000px; height: 1200px; }

  .card {
    position: absolute; left: 50px; width: 900px;
    border-radius: 22px;
    box-shadow: 0 10px 26px var(--shadow);
    overflow: hidden;
  }
  .card--front {
    top: 50px; height: 500px;
    background: linear-gradient(90deg, var(--card-front) 55%, var(--card-front-edge) 100%);
    color: var(--ink-dark);
  }
  .card--back {
    top: 650px; height: 498px;
    background: var(--card-back);
    color: var(--ink-light);
  }
  .abs { position: absolute; line-height: 1; white-space: nowrap; }

  /* Front */
  .brand-mark {
    left: 48px; top: 156px; width: 84px; height: 84px;
    border-radius: 50%; background: var(--brand-red);
  }
  .brand-name {
    left: 148px; top: 150px; font-size: 58px; font-weight: 500;
    color: var(--ink-dark); letter-spacing: 1px;
  }
  .person { right: 62px; top: 100px; text-align: right; }
  .person__name { font-size: 34px; font-weight: 600; display: block; }
  .person__role { font-size: 25px; font-weight: 400; display: block; margin-top: 14px; }
  .contact {
    right: 62px; top: 318px; text-align: right;
    font-size: 25px; font-weight: 400; line-height: 39px;
  }
  .contact li { list-style: none; }

  /* Back */
  .back-mark {
    left: 62px; top: 150px; width: 150px; height: 150px;
    border-radius: 50%; background: var(--brand-grey);
  }
  .back-name {
    left: 236px; top: 172px; font-size: 112px; font-weight: 500;
    color: var(--brand-grey); letter-spacing: 2px;
  }
  .venue { left: 469px; }
  .venue__type { display: block; font-size: 38px; font-weight: 400; color: var(--brand-red); }
  .venue__place { display: block; font-size: 28px; font-weight: 400; margin-top: 16px; }
  .venue__address { display: block; font-size: 20px; font-weight: 400; margin-top: 10px; }
  .venue--outdoor { top: 40px; }
  .venue--personal { top: 342px; }
</style>
</head>
<body>
<main class="canvas">
  <section class="card card--front" aria-label="Card front">
    <span class="abs brand-mark" aria-hidden="true"></span>
    <span class="abs brand-name">KINETRIXX FITNESS</span>

    <div class="abs person">
      <span class="person__name">Gareth Pollwick</span>
      <span class="person__role">Director</span>
    </div>

    <ul class="abs contact">
      <li>ABN: 48392057</li>
      <li>T: 0458 702 136</li>
      <li>E: kinetrixx@postnest.com</li>
      <li>W: kinetrixxfitness.com.au</li>
    </ul>
  </section>

  <section class="card card--back" aria-label="Card back">
    <span class="abs back-mark" aria-hidden="true"></span>
    <span class="abs back-name">KINETRIXX</span>

    <div class="abs venue venue--outdoor">
      <span class="venue__type">Outdoor Group Training</span>
      <span class="venue__place">Ferndale Archers Club</span>
      <span class="venue__address">42 Tillbrook Road, Scarborough WA 6019</span>
    </div>

    <div class="abs venue venue--personal">
      <span class="venue__type">Personal Training</span>
      <span class="venue__place">Amberline Fitness Studio</span>
      <span class="venue__address">518 Wrenhollow Street, Scarborough WA 6019</span>
    </div>
  </section>
</main>
</body>
</html>
```